Im want a website LIKE KVT's and FieldCrest.com's with product payment options like Trovella's

I need a website LIKE KVT with a header made EXACTLY LIKE THAT OF FIELDCRESTS .

The front page photo should be like that of FIELDCREST's webpage as well.

The name of the website will be called "M.K. (Maravel Key)".

We will be targeting ALL MARKETS in a small town in central Panama and charging businesses "listing fees" like a phone book does but also providing informational blogs, news, and other interesting activities.

THIS IS A MULTI PAGE WEBSITE

THIS IS WHERE KVT's website meets Zentaro/FieldCrest.

Once the layout is built I will tweak and modify, add information, and upload items for sale.

Here is a list of specific categories that should be listed out above the front page header image/search bar

-- Home -- News -- Travel -- Activities -- Shop & Dine -- Store -- More... --

These categories should be spread across the bottom of the page in three sections:

WHATS SO GREAT ABOUT (Maravel Key),
HAND PICKED TOURS
ACTIVITIES etc.

Also lets use www.Trovella.example 's
"HOT DESTINATIONS"
"BEAT THE BEST PRICES IN BOQUETE"
"OCTOBERS INSIDER PICKS"
"TOP DESTINATIONS"
and spread them in four sections side-by-side near the bottom of the page.

Overall I would like to see the finished product to be something LIKE KVT's and FieldCrests.

WE NEED ONLINE PAYMENT OPTIONS LIKE ZENTARO'S WEBSITE HAS

This will be a desktop website but should be very mobile friendly as well.

-roderick

P.S. Good luck!

If it isn't already too late to change the website name, the name of the website should be "Maravel Key". Added Friday, October 9, 2015

What do you guys think the budget should be to win this? Added Saturday, October 10, 2015

www.lunavista.example is the most amazing simple site. Whoever can make me a replica with my specifications will win immediately!!!! Added Sunday, October 18, 2015

OMG www.lunavista.example is the bomb!So simple and elegant. Whoever can make me an EXACT REPLICA OF WWW.LUNAVISTA.EXAMPLE as my site with the specifications mentioned in my brief will take home the $825.00 immediately! Good luck amigos! Added Sunday, October 18, 2015

Does anybody know how to add recurring monthly billing options on this website? Added Sunday, October 18, 2015

ALL MARKETS

Product

Coded - Design and coding required

5+ page

• Paywell payment options.
• I must be able to add and remove photos/text and video from the HTML files in the page.
• Be creative my friends, and may the odds be forever in your favor!
• I added some photos of a good layout for our page below.

```html
<!DOCTYPE html>
<html lang="en">
<head>
<meta charset="utf-8">
<title>Maravel Key — Home</title>
<link rel="stylesheet" href="https://fonts.googleapis.com/css2?family=Open+Sans:wght@400;600;700&display=swap">
<style>
:root{
  --blue:#1a8cc8;
  --blue-dark:#0f5e88;
  --footer:#1b86bd;
  --ink:#444;
  --muted:#888;
  --line:#dedede;
  --grey-bg:#eeeeee;
  --white:#fff;
}
*{box-sizing:border-box;margin:0;padding:0}
html,body{width:1200px;height:2512px;overflow:hidden}
body{font-family:"Open Sans",Arial,sans-serif;color:var(--ink);background:var(--white);font-size:13px;line-height:1.5}
.wrap{width:864px;margin:0 auto;position:relative}
a{color:inherit;text-decoration:none}
ul{list-style:none}

/* header */
.site-header{height:144px;position:relative}
.site-header .wrap{height:144px}
.brand{position:absolute;left:0;top:26px;display:flex;align-items:center;gap:10px}
.brand-mark{width:30px;height:30px;border-radius:50%;background:var(--blue)}
.brand-name{font-size:28px;font-weight:700;color:var(--blue)}
.util-links{position:absolute;right:0;top:20px;display:flex;gap:26px;font-size:11px;color:var(--muted)}
.util-links span{display:flex;align-items:center;gap:6px}
.util-links i{width:12px;height:12px;border-radius:50%;background:var(--blue);display:inline-block}
.main-nav{position:absolute;right:0;top:96px;display:flex;gap:28px;font-size:13px;color:#666}
.main-nav a.active{color:var(--blue);border-bottom:2px solid var(--blue);padding-bottom:6px}

/* hero */
.hero{height:596px;position:relative;background:linear-gradient(180deg,#cfe3ef 0%,#9fc4da 45%,#3d8db8 72%,#d9cfc0 100%)}
.hero-search{position:absolute;left:600px;top:120px;width:460px;height:112px;background:rgba(40,50,60,.55);padding:18px 22px}
.hero-search h2{color:#fff;font-weight:400;font-size:20px;margin-bottom:12px}
.search-row{display:flex}
.search-row .field{flex:1;height:36px;background:#fff;font-size:11px;color:#999;padding:9px 10px}
.search-row .btn{width:92px;height:36px;background:var(--blue);color:#fff;font-size:11px;font-weight:700;display:flex;align-items:center;justify-content:center}

/* features */
.features{height:112px;border-bottom:1px solid var(--line)}
.features .wrap{display:flex;align-items:center;height:112px;gap:22px}
.features .intro{width:130px;font-size:11px;color:var(--muted);line-height:1.35}
.feature{display:flex;gap:8px;align-items:flex-start;width:130px}
.feature .ico{width:24px;height:24px;border-radius:50%;border:2px solid var(--blue);flex:none}
.feature b{display:block;color:var(--blue);font-size:11px}
.feature small{font-size:9px;color:var(--muted);line-height:1.2;display:block}

/* section heads */
.section-head{display:flex;justify-content:space-between;align-items:center;height:56px;border-bottom:1px solid var(--line);margin-bottom:22px}
.section-head h3{color:var(--blue);font-size:20px;font-weight:600}
.see-more{font-size:10px;color:var(--blue-dark)}

/* tiles */
.explore{background:var(--grey-bg);padding:20px 0 40px}
.tile-grid{display:grid;grid-template-columns:repeat(3,280px);gap:16px 12px}
.tile{height:204px;position:relative}
.tile .cap{position:absolute;left:0;right:0;bottom:0;background:rgba(20,130,170,.75);color:#fff;font-size:11px;padding:8px 12px;line-height:1.35}
.t1{background:linear-gradient(160deg,#2a8fb8,#0c5f86)}
.t2{background:linear-gradient(160deg,#8bb8d6,#3f7a3a)}
.t3{background:linear-gradient(160deg,#7fb7d8,#8a6a3e)}
.t4{background:linear-gradient(160deg,#6f9a4f,#b0543e)}
.t5{background:linear-gradient(160deg,#5b8fb4,#c6a06a)}
.t6{background:linear-gradient(160deg,#4f7e3a,#2f8ab5)}
.t1 .cap{top:40px;bottom:auto;background:none;font-size:13px}

.picks{display:grid;grid-template-columns:repeat(3,280px);gap:12px;margin-top:40px}
.picks h4{color:var(--blue);font-size:14px;font-weight:700;margin-bottom:10px}
.picks p,.picks li{font-size:11px;color:#666;line-height:1.6}
.picks li{padding-left:14px;position:relative}
.picks li:before{content:"";position:absolute;left:0;top:6px;width:6px;height:6px;border-radius:50%;background:var(--blue)}

/* cards */
.featured{padding:20px 0 0;height:672px}
.card-row{display:grid;grid-template-columns:repeat(3,280px);gap:12px}
.card{background:#fff;box-shadow:0 1px 4px rgba(0,0,0,.18)}
.card .photo{height:160px}
.c1{background:linear-gradient(170deg,#a9c9e0,#5d6b3a)}
.c2{background:linear-gradient(170deg,#d7b36a,#8b4e3a)}
.c3{background:linear-gradient(170deg,#b8d3e6,#5f8a3e)}
.card .label{background:#f3f3f3;text-align:center;font-size:12px;font-weight:600;padding:5px 0;color:#555}
.card p{font-size:11px;color:#666;padding:14px 16px 22px;text-align:center;line-height:1.5}
.featured .more{text-align:right;margin-top:18px}

/* footer */
.site-footer{background:var(--footer);height:184px;color:#e6f3fa;margin-top:-2px}
.site-footer .wrap{display:flex;height:184px;padding-top:18px;gap:26px}
.f-about{width:200px}
.f-about .brand-name{font-size:22px;color:#fff}
.f-about p{font-size:9px;line-height:1.4;margin-top:6px}
.pay{display:flex;gap:4px;margin-top:8px;align-items:center;font-size:10px}
.pay i{width:22px;height:14px;background:#d9ecf6;display:inline-block}
.f-col h5{font-size:10px;color:#fff;margin-bottom:6px}
.f-col li{font-size:9px;line-height:1.6}
.f-links{width:110px}
.socials{display:flex;gap:6px;margin-bottom:16px}
.socials i{width:20px;height:20px;background:#d9ecf6;display:block}
.mobile{width:26px;height:40px;border:2px solid #fff;border-radius:4px}
.f-find{margin-left:auto;width:260px;background:var(--blue-dark);padding:12px 14px;margin-top:-18px;height:184px}
.f-find h5{color:#fff;font-size:11px;margin-bottom:6px}
.f-find .field{height:20px;background:#fff;font-size:9px;color:#999;padding:3px 6px;margin-bottom:10px}
.cities{display:grid;grid-template-columns:1fr 1fr;font-size:9px;line-height:1.55}
.copyright{height:36px;background:#136f9e;color:#cde6f3;font-size:9px;text-align:center;line-height:36px}
</style>
</head>
<body>

<header class="site-header">
  <div class="wrap">
    <a class="brand" href="#"><span class="brand-mark"></span><span class="brand-name">Maravel Key</span></a>
    <div class="util-links"><span><i></i>Hello Register</span><span><i></i>Log in / Register</span><span><i></i>Help</span></div>
    <nav class="main-nav">
      <a class="active" href="#">Home</a><a href="#">Tours</a><a href="#">Lodging</a><a href="#">Destinations</a><a href="#">Classifieds</a><a href="#">Blog</a><a href="#">Contact Us</a>
    </nav>
  </div>
</header>

<section class="hero" role="img" aria-label="Photo of a smiling couple in sunglasses by the sea with a city skyline">
  <div class="hero-search">
    <h2>Let the activities begin !</h2>
    <div class="search-row"><div class="field">Search the Destinations, Attractions and Tours</div><div class="btn">SEARCH</div></div>
  </div>
</section>

<section class="features">
  <div class="wrap">
    <div class="intro">What's so great about Maravel Key?</div>
    <div class="feature"><span class="ico"></span><div><b>HANDPICKED</b><small>Tours &amp; activities</small></div></div>
    <div class="feature"><span class="ico"></span><div><b>VERIFIED</b><small>Reviews &amp; photos</small></div></div>
    <div class="feature"><span class="ico"></span><div><b>VIP</b><small>Access</small></div></div>
    <div class="feature"><span class="ico"></span><div><b>LOW PRICES</b><small>Guaranteed</small></div></div>
    <div class="feature"><span class="ico"></span><div><b>24/7 SUPPORT</b><small>Call or email</small></div></div>
  </div>
</section>

<section class="explore">
  <div class="wrap">
    <div class="section-head"><h3>Lorem Ipsum</h3><a class="see-more" href="#">See More &#9656;</a></div>
    <div class="tile-grid">
      <div class="tile t1" role="img" aria-label="Photo of clear blue ocean water"><div class="cap">Lorem Ipsum is simply dummy text of the printing and typesetting industry.<br><br><b>See More &#9656;</b></div></div>
      <div class="tile t2" role="img" aria-label="Photo of green mountains and valley"><div class="cap">Lorem Ipsum is simply dummy text of the printing and typesetting industry.</div></div>
      <div class="tile t3" role="img" aria-label="Photo of a thatched hut by the water"><div class="cap">Lorem Ipsum is simply dummy text of the printing and typesetting industry.</div></div>
      <div class="tile t4" role="img" aria-label="Photo of a group of travellers outdoors"><div class="cap">Lorem Ipsum is simply dummy text of the printing and typesetting industry.</div></div>
      <div class="tile t5" role="img" aria-label="Photo of a rafting tour on a river"><div class="cap">Lorem Ipsum is simply dummy text of the printing and typesetting industry.</div></div>
      <div class="tile t6" role="img" aria-label="Photo of tropical coastline with forest"><div class="cap">Lorem Ipsum is simply dummy text of the printing and typesetting industry.</div></div>
    </div>

    <div class="picks">
      <div>
        <h4>October Insider's Pick</h4>
        <p>Suspendisse dictum quam luctus et sapien. Nunc feugiat pellentesque et dui volutpat. Duis vitae mi sed neque tempus pretium. Etiam blandit neque a lorem ultrices, nec tempor nibh.</p>
      </div>
      <div>
        <h4>Hot Destinations</h4>
        <ul>
          <li>Suspendisse dictum quam luctus</li>
          <li>Sed dapibus lacus</li>
          <li>Quisque vestibulum consequat</li>
          <li>Nam eu ligula vulputate pulvinar</li>
          <li>Curabitur at rhoncus quam</li>
        </ul>
      </div>
      <div>
        <h4>Beat the Crowds in Europe</h4>
        <p>Curabitur at rhoncus quam et ultrices sed nunc tempor. Aliquam in leo nisi. Fusce posuere justo id metus semper molestie. Fusce posuere justo id metus semper molestie.</p>
      </div>
    </div>
  </div>
</section>

<section class="featured">
  <div class="wrap">
    <div class="section-head"><h3>Lorem Ipsum</h3><a class="see-more" href="#">See More &#9656;</a></div>
    <div class="card-row">
      <article class="card"><div class="photo c1" role="img" aria-label="Photo of a hillside lodge"></div><div class="label">Lorem Ipsum</div><p>Lorem Ipsum is simply dummy text of the printing and typesetting industry. Lorem Ipsum has been the industry's standard dummy text ever since the 1500s.</p></article>
      <article class="card"><div class="photo c2" role="img" aria-label="Photo of a local street market"></div><div class="label">Lorem Ipsum</div><p>Lorem Ipsum is simply dummy text of the printing and typesetting industry. Lorem Ipsum has been the industry's standard dummy text ever since the 1500s.</p></article>
      <article class="card"><div class="photo c3" role="img" aria-label="Photo of horseback riders in the hills"></div><div class="label">Lorem Ipsum</div><p>Lorem Ipsum is simply dummy text of the printing and typesetting industry. Lorem Ipsum has been the industry's standard dummy text ever since the 1500s.</p></article>
    </div>
    <div class="more"><a class="see-more" href="#">See More &#9656;</a></div>
  </div>
</section>

<footer>
  <div class="site-footer">
    <div class="wrap">
      <div class="f-about">
        <div class="brand-name">Maravel Key</div>
        <p>Lorem Ipsum is simply dummy text of the printing and typesetting industry. Lorem Ipsum has been the standard dummy text ever since the 1500s, when an unknown printer took a galley of type.</p>
        <div class="pay">Paywell <i></i><i></i><i></i><i></i></div>
      </div>
      <div class="f-col f-links">
        <h5>QUICK LINKS</h5>
        <ul><li>Home</li><li>About Us</li><li>Services</li><li>Blog</li><li>Contact Us</li></ul>
      </div>
      <div class="f-col">
        <h5>SOCIAL</h5>
        <div class="socials"><i></i><i></i><i></i><i></i></div>
        <h5>MOBILE</h5>
        <div class="mobile"></div>
      </div>
      <div class="f-find">
        <h5>FIND YOUR NEXT ACTIVITY!</h5>
        <div class="field">Search</div>
        <h5>TOP 10 CITIES</h5>
        <div class="cities">
          <span>Amsterdam Tours</span><span>New York Tours</span>
          <span>Dublin Tours</span><span>Paris Tours</span>
          <span>Honolulu Tours</span><span>Rome Tours</span>
          <span>Las Vegas Tours</span><span>San Francisco Tours</span>
          <span>London Tours</span><span>Sydney Tours</span>
        </div>
      </div>
    </div>
  </div>
  <div class="copyright">Copyright © 2015 Maravel Key. All rights reserved.</div>
</footer>

</body>
</html>
```